Apartment Investor Business Card Design

Need a new business card designed for my multifamily investment company

Industry/Entity Type

Real Estate

Contact Information for Business Card

Marlow Pickett - President & CEO
Brightfield Capital, LLC
4870 North 52nd Avenue, Ste 150
Omaha, NE 68231
(402) 555-0193
Marlow@brightfieldcapitalmidwest.example
Www.BrightfieldCapitalMidwest.example

Colors
3176b5

```html
<!DOCTYPE html>
<html lang="en">
<head>
<meta charset="utf-8">
<title>Brightfield Capital – Business Card</title>
<link rel="stylesheet" href="https://fonts.googleapis.com/css2?family=Cinzel:wght@400;600&family=Lato:wght@400;700&display=swap">
<style>
  :root{
    --brand-blue:#3176b5;
    --band-blue:#4d82c6;
    --band-gray:#9a9a9a;
    --ink:#2b2b2b;
    --paper:#ffffff;
    --back-gray:#9b9b9b;
    --back-gray-light:#a8a8a8;
    --stage:#e6e7e9;
  }
  html,body{margin:0;padding:0;overflow:hidden}
  body{width:1200px;height:782px;background:var(--stage);position:relative;font-family:"Lato",sans-serif}
  .card{position:absolute;width:540px;height:309px;top:236px;overflow:hidden;box-shadow:0 6px 18px rgba(0,0,0,.18)}
  .card--front{left:40px;background:var(--paper)}
  .card--back{left:620px;background:var(--back-gray)}

  .holder{position:absolute;left:30px;top:28px}
  .holder__name{font-family:"Cinzel",serif;font-weight:600;color:var(--brand-blue);font-size:19px;letter-spacing:.5px;margin:0}
  .holder__title{font-size:12px;color:var(--ink);margin:2px 0 0}

  .contacts{position:absolute;left:30px;top:180px;list-style:none;margin:0;padding:0;font-size:13.5px;color:var(--ink);line-height:20px}
  .contacts li{display:flex;align-items:center;gap:6px}
  .contacts svg{width:11px;height:11px;flex:none;fill:var(--brand-blue)}

  .brand{position:absolute;right:32px;top:128px;display:flex;align-items:center;gap:8px}
  .brand__mark{width:12px;height:12px;background:var(--brand-blue)}
  .brand__name{font-family:"Cinzel",serif;font-weight:400;font-size:22px;color:var(--ink);letter-spacing:1px}

  .address{position:absolute;right:32px;top:190px;text-align:left;font-size:14px;color:var(--ink);line-height:18px}
  .address__company{color:var(--brand-blue);font-weight:700}

  .band{position:absolute;bottom:0;left:0;width:100%;height:62px}

  .back__pattern{position:absolute;inset:0;background:linear-gradient(135deg,var(--back-gray-light),var(--back-gray))}
  .back__brand{position:absolute;left:50%;top:50%;transform:translate(-50%,-50%);display:flex;align-items:center;gap:6px}
  .back__mark{width:9px;height:9px;background:var(--paper)}
  .back__name{font-family:"Cinzel",serif;font-size:14px;color:var(--paper);letter-spacing:1px}
</style>
</head>
<body>

<section class="card card--front" aria-label="Business card front">
  <div class="holder">
    <h1 class="holder__name">Marlow Pickett</h1>
    <p class="holder__title">President &amp; CEO</p>
  </div>

  <ul class="contacts">
    <li><svg viewBox="0 0 12 12" aria-hidden="true"><path d="M2 1h3l1 3-2 1a7 7 0 0 0 3 3l1-2 3 1v3a1 1 0 0 1-1 1A10 10 0 0 1 1 2a1 1 0 0 1 1-1z"/></svg>(402) 555-0193</li>
    <li><svg viewBox="0 0 12 12" aria-hidden="true"><path d="M1 2h10v8H1z M1.5 2.5 6 6.5l4.5-4" stroke="#fff" stroke-width="1"/></svg>Marlow@brightfieldcapitalmidwest.example</li>
    <li><svg viewBox="0 0 12 12" aria-hidden="true"><circle cx="6" cy="6" r="5.5"/></svg>Www.BrightfieldCapitalMidwest.example</li>
  </ul>

  <div class="brand">
    <span class="brand__mark" aria-hidden="true"></span>
    <span class="brand__name">Brightfield Capital</span>
  </div>

  <address class="address" style="font-style:normal">
    <div class="address__company">Brightfield Capital, LLC</div>
    <div>4870 North 52nd Avenue</div>
    <div>Ste 150 Omaha, NE 68231</div>
  </address>

  <svg class="band" viewBox="0 0 540 62" preserveAspectRatio="none" aria-hidden="true">
    <polygon points="0,0 280,0 285,28 0,28" fill="var(--band-blue)"/>
    <polygon points="288,18 540,34 540,56 288,56" fill="var(--band-gray)"/>
  </svg>
</section>

<section class="card card--back" aria-label="Business card back">
  <div class="back__pattern" role="img" aria-label="Repeating faint brand pattern on gray"></div>
  <div class="back__brand">
    <span class="back__mark" aria-hidden="true"></span>
    <span class="back__name">Brightfield Capital</span>
  </div>
</section>

</body>
</html>
```